Stationery Design Project

KT7 Staffing requires letterhead and business card designs for a company based in London. Just like the name, we're a management resourcing company, providing resources to third party companies. You can see www.kt7staffing-example.com for ideas on existing colour schemes and design concepts that have been implimented and agreed to. Ultimately the design should broadcast professionalism, safety and the concept of growth.

Target Market(s)

Financial institutes; friendly societies (All UK based)

Industry/Entity Type

Safety

Requirements
Must have
• Files produced should be print ready; and the text in them editable (eg address, name etc)

```html
<!DOCTYPE html>
<html lang="en">
<head>
<meta charset="utf-8">
<title>KT7 Staffing – Stationery</title>
<link href="https://fonts.googleapis.com/css2?family=Noto+Sans:wght@400;700&family=Open+Sans:wght@400;600&display=swap" rel="stylesheet">
<style>
  :root {
    --teal-dark: #2f8c91;
    --teal: #4aa3b4;
    --teal-soft: #80b9c7;
    --card-blue: #3aa2bf;
    --card-glow: #6cc4d8;
    --ink: #3a3a3a;
    --grey-text: #8a8a8a;
    --stage-light: #ffffff;
    --stage-dark: #dedede;
    --paper: #ffffff;
  }
  * { box-sizing: border-box; margin: 0; padding: 0; }
  html, body { width: 1200px; height: 900px; overflow: hidden; }
  body {
    position: relative;
    background: radial-gradient(ellipse at 78% 40%, var(--stage-light) 0%, #f3f3f3 35%, var(--stage-dark) 100%);
    font-family: "Open Sans", sans-serif;
  }

  /* Brand lockup (text only) */
  .brand { display: flex; align-items: center; gap: 6px; font-family: "Noto Sans", sans-serif; font-weight: 700; color: var(--teal-dark); white-space: nowrap; }
  .brand-square { width: 10px; height: 10px; background: var(--teal-soft); flex: none; }

  /* Letterhead */
  .letterhead {
    position: absolute; left: 46px; top: 43px; width: 613px; height: 792px;
    background: var(--paper); box-shadow: 0 0 4px rgba(0,0,0,.08);
  }
  .letterhead .brand { position: absolute; left: 27px; top: 52px; font-size: 24px; }
  .letterhead .brand-square { width: 16px; height: 16px; }
  .letter-body {
    position: absolute; left: 93px; top: 195px; width: 447px;
    font-family: "Noto Sans", sans-serif; font-size: 9.6px; line-height: 11.7px;
    color: var(--ink); text-align: justify; hyphens: auto;
  }
  .letter-body p + p { margin-top: 11.7px; }
  .signature { position: absolute; left: 98px; top: 592px; width: 96px; height: 71px; background: linear-gradient(135deg, #f4f4f4, #e9e9e9); }
  .letter-address {
    position: absolute; left: 26px; top: 731px; font-size: 9.2px; line-height: 13px;
    color: #555; font-style: normal; white-space: nowrap;
  }
  .letter-address .label { color: var(--teal); }
  .letter-rule { position: absolute; left: 0; right: 0; top: 768px; height: 3px; background: var(--teal-dark); }
  .letter-band {
    position: absolute; left: 0; right: 0; top: 773px; height: 19px; background: var(--teal-soft);
    color: #fff; font-size: 9px; line-height: 19px; text-align: right; padding-right: 16px;
  }

  /* Business card front */
  .card-front {
    position: absolute; left: 768px; top: 82px; width: 252px; height: 143px; border-radius: 9px;
    background: radial-gradient(circle at 42% 45%, var(--card-glow) 0%, var(--card-blue) 60%, #349bb8 100%);
    display: flex; align-items: center; justify-content: center;
  }
  .card-front .brand { color: #fff; font-size: 17px; }
  .card-front .brand-square { background: #fff; }

  /* Business card back */
  .card-back {
    position: absolute; left: 766px; top: 252px; width: 252px; height: 143px; border-radius: 9px;
    background: var(--paper); overflow: hidden; box-shadow: 0 0 3px rgba(0,0,0,.06);
  }
  .card-back .brand { position: absolute; left: 11px; top: 18px; font-size: 13px; }
  .card-back .brand-square { width: 8px; height: 8px; }
  .card-address { position: absolute; left: 149px; top: 55px; font-size: 5.5px; line-height: 8px; color: var(--grey-text); }
  .card-person { position: absolute; left: 29px; top: 80px; }
  .card-name { font-size: 9px; font-weight: 600; color: var(--teal); }
  .card-role { font-size: 5.5px; color: var(--grey-text); }
  .card-contacts { position: absolute; left: 149px; top: 77px; list-style: none; font-size: 5.5px; line-height: 9px; color: var(--grey-text); }
  .card-contacts li { display: flex; align-items: center; gap: 4px; }
  .card-contacts svg { width: 6px; height: 6px; fill: var(--teal-dark); flex: none; }
  .card-rule { position: absolute; left: 0; right: 0; top: 129px; height: 2px; background: var(--teal-dark); }
  .card-band { position: absolute; left: 0; right: 0; top: 132px; height: 11px; background: var(--teal-soft); }
</style>
</head>
<body>

<section class="letterhead">
  <div class="brand"><span class="brand-square"></span>KT7 Staffing</div>

  <div class="letter-body">
    <p>Lorem ipsum dolor sit amet, consectetuer adipiscing elit. Pellentesque tristique elementum sem. Quisque eget erat ac lectus sodales faucibus. Nam commodo est. Cras consequat faucibus velit. Nam ac magna. Sed et ligula. Nam volutpat, elit ac facilisis tempor, neque augue euismod leo, sit amet molestie sem est eu libero. Nulla facilisi. Pellentesque sit amet odio. Curabitur a leo consectetuer leo blandit porttitor. Pellentesque velit quam, gravida at, pharetra eu, convallis non, sem. Aenean tempor nibh at purus. Pellentesque porta. Suspendisse congue, lacus sit amet imperdiet imperdiet, urna massa rutrum urna, id elementum tellus diam quis risus.</p>
    <p>In dui turpis, varius vitae, tincidunt id, consequat ut, leo. Donec tincidunt tristique odio. Nulla erat felis, euismod nec, fringilla non, aliquet et, magna. Nulla at magna quis nisi pretium vehicula. Pellentesque habitant morbi tristique senectus et netus et malesuada fames ac turpis egestas. Class aptent taciti sociosqu ad litora torquent per conubia nostra, per inceptos himenaeos. In vel quam. Phasellus varius convallis purus. In non turpis. Nam sed risus. Etiam non neque at nisl gravida porttitor. Donec leo dolor, feugiat ut, pharetra et, porttitor a, metus. Suspendisse laoreet magna vel elit. Ut est augue, fermentum ac, molestie at, vestibulum et, urna.</p>
    <p>Nunc purus. Cras auctor. In ornare neque id ipsum. Nulla tincidunt, diam sit amet viverra euismod, sapien augue fringilla neque, at pellentesque felis tortor vel enim. Etiam dignissim. Sed a tortor vel nisi euismod ultricies. Donec molestie congue lectus. Integer sed turpis a tortor imperdiet consequat. Maecenas molestie placerat urna. Sed pede enim, sollicitudin nec, pretium nec, sollicitudin a, felis. In hac habitasse platea dictumst. Nam facilisis, tellus non scelerisque placerat, turpis turpis semper ante, euismod imperdiet augue nisi et neque. Vivamus tincidunt.</p>
    <p>Nulla lobortis ultricies nulla. Pellentesque purus mi, consequat quis, hendrerit sed, imperdiet non, eros. Nullam urna est, vehicula nec, cursus nec, dignissim sit amet, risus. Duis molestie, tellus sit amet laoreet ullamcorper, urna nisi fringilla ante, at rhoncus justo dolor vel dui. Nam hendrerit luctus lorem. Aenean tempor, metus vel posuere gravida, arcu nunc imperdiet tellus, ut blandit sem magna a turpis. Vivamus in neque. Lorem ipsum dolor sit amet, consectetuer adipiscing elit. Duis tristique tortor id nisl feugiat posuere. Maecenas posuere nisi ac risus. Nunc hendrerit. Praesent porta tempus ligula. Morbi in leo. Curabitur sapien nulla, cursus eget, faucibus in, porttitor et, odio. Praesent sed justo sed arcu commodo feugiat. Duis facilisis nulla ut eros. Cras libero. Donec mollis consectetuer metus. Praesent odio.</p>
  </div>

  <div class="signature" role="img" aria-label="Handwritten signature of the sender"></div>

  <address class="letter-address">
    48 Harlow Crescent, Suite 3, London EC2A 4PL<br>
    <span class="label">Phone.</span> 020-7946-0132 &nbsp;<span class="label">Fax.</span> 020-7946-0132
  </address>
  <div class="letter-rule"></div>
  <div class="letter-band">www.kt7staffing-example.com</div>
</section>

<section class="card-front">
  <div class="brand"><span class="brand-square"></span>KT7 Staffing</div>
</section>

<section class="card-back">
  <div class="brand"><span class="brand-square"></span>KT7 Staffing</div>
  <div class="card-address">48 Harlow Crescent, Suite 3<br>London EC2A 4PL</div>
  <div class="card-person">
    <div class="card-name">Daniel Marsh</div>
    <div class="card-role">Marketing Manager</div>
  </div>
  <ul class="card-contacts">
    <li><svg viewBox="0 0 10 10"><path d="M1 3c0-1 1-2 4-2s4 1 4 2v1H7V3H3v1H1zM2 5h6l1 4H1z"/></svg>0044 (0)20 7946 0821</li>
    <li><svg viewBox="0 0 10 10"><rect x="1" y="6" width="2" height="4"/><rect x="4" y="3" width="2" height="7"/><rect x="7" y="0" width="2" height="10"/></svg>0044 (0)7700 900 415</li>
    <li><svg viewBox="0 0 10 10"><rect x="2" y="0" width="6" height="3"/><rect x="0" y="3" width="10" height="5"/><rect x="2" y="6" width="6" height="4" fill="#fff" stroke="#2f8c91"/></svg>0044 (0)20 7946 0822</li>
    <li><svg viewBox="0 0 10 10"><path d="M0 2h10v6H0z" fill="none" stroke="#2f8c91"/><path d="M0 2l5 4 5-4" fill="none" stroke="#2f8c91"/></svg>info@kt7staffing-example.com</li>
    <li><svg viewBox="0 0 10 10"><path d="M5 0l5 5H8v5H2V5H0z"/></svg>www.kt7staffing-example.com</li>
  </ul>
  <div class="card-rule"></div>
  <div class="card-band"></div>
</section>

</body>
</html>
```